Baseball Themed Birthday Invitation

Hello,

I need a birthday invitation design created for me. I will be taking the design, getting it manufactured in bulk and selling them.

These types of invitations are not custom, but rather will have "fill in fields". Please see attachment as an example (wild one example attached). The mandatory fill in fields are : Name, Location, Date, Time, RSVP.

The target age will be 4-12

The size is 7" x 5".

This project is for a Baseball themed party design. I attached an example invitation (baseball design) to show one i really like. This design does not include the fill in fields, but i like the use of fonts/colors design. That being said, I am open to seeing different concepts and designs.

Thank you!

Target Market(s)

Boys 4-12 years old

Requirements
Must have
• Fill in fields as discussed in brief.

```html
<!DOCTYPE html>
<html lang="en">
<head>
<meta charset="utf-8">
<title>Batter Up! Baseball Birthday Invitation</title>
<link rel="stylesheet" href="https://fonts.googleapis.com/css2?family=Jost:wght@500;600;700&display=swap">
<style>
  :root {
    --navy: #2b4a6e;
    --red: #d2352b;
    --panel: rgba(250, 248, 248, 0.82);
    --leather-light: #e9e6e6;
    --leather-mid: #c9c4c6;
    --stitch: #c96a6a;
    --bat-wood: #c48d55;
    --bat-dark: #6e4a2a;
  }
  * { margin: 0; padding: 0; box-sizing: border-box; }
  html, body { width: 857px; height: 1200px; overflow: hidden; background: #ffffff; }
  .invitation {
    position: relative;
    width: 857px;
    height: 1200px;
    overflow: hidden;
    font-family: "Jost", "Futura", sans-serif;
    color: var(--navy);
  }
  .backdrop {
    position: absolute;
    inset: 0;
    background:
      radial-gradient(circle at 20% 15%, rgba(201,106,106,0.35), transparent 40%),
      radial-gradient(circle at 85% 75%, rgba(201,106,106,0.3), transparent 45%),
      linear-gradient(160deg, var(--leather-light), var(--leather-mid));
  }
  .card-frame {
    position: absolute;
    left: 53px;
    top: 87px;
    width: 752px;
    height: 1052px;
    border: 8px solid var(--red);
    background: var(--panel);
  }
  .text-line {
    position: absolute;
    left: 0;
    width: 857px;
    text-align: center;
    font-weight: 600;
    line-height: 1;
    white-space: nowrap;
  }
  .headline { top: 142px; font-size: 82px; font-weight: 700; color: var(--navy); }
  .tagline { top: 234px; font-size: 44px; color: var(--red); letter-spacing: 0.5px; }
  .honoree { top: 303px; font-size: 48px; color: var(--navy); letter-spacing: 1px; }
  .fill-rule {
    position: absolute;
    height: 2.5px;
    background: var(--navy);
  }
  .field-label {
    position: absolute;
    font-size: 22px;
    font-weight: 600;
    line-height: 1;
    text-align: center;
    color: var(--navy);
  }
  .art {
    position: absolute;
    border-radius: 6px;
  }
  .art-icon-batter { left: 416px; top: 580px; width: 40px; height: 46px; background: linear-gradient(var(--navy), #3d5f86); opacity: 0.85; }
  .art-batter { left: 144px; top: 995px; width: 100px; height: 103px; background: linear-gradient(160deg, var(--navy), #3d5f86); opacity: 0.8; }
  .art-fielder { left: 613px; top: 994px; width: 87px; height: 104px; background: linear-gradient(160deg, var(--navy), #3d5f86); opacity: 0.8; }
  .art-bats { left: 316px; top: 982px; width: 223px; height: 201px; background: linear-gradient(180deg, var(--bat-wood), var(--bat-dark)); opacity: 0.75; }
</style>
</head>
<body>
<main class="invitation">
  <div class="backdrop" role="img" aria-label="Close-up photograph of a pile of white baseballs with red stitching"></div>
  <section class="card-frame"></section>

  <h1 class="text-line headline">BATTER UP!</h1>
  <p class="text-line tagline">JOIN US TO CELEBRATE</p>
  <p class="text-line honoree">OUR ROOKIE OF THE YEAR</p>

  <div class="fill-rule" style="left:127px; top:460px; width:600px;"></div>
  <span class="field-label" style="left:0; width:857px; top:473px;">NAME</span>

  <div class="fill-rule" style="left:129px; top:602px; width:274px;"></div>
  <div class="art art-icon-batter" role="img" aria-label="Small silhouette of a batter hitting a ball"></div>
  <div class="fill-rule" style="left:453px; top:602px; width:274px;"></div>
  <span class="field-label" style="left:134px; width:200px; top:616px;">DATE</span>
  <span class="field-label" style="left:473px; width:200px; top:616px;">TIME</span>

  <div class="fill-rule" style="left:127px; top:740px; width:600px;"></div>
  <span class="field-label" style="left:0; width:857px; top:754px;">LOCATION</span>

  <div class="fill-rule" style="left:127px; top:893px; width:600px;"></div>
  <span class="field-label" style="left:0; width:857px; top:916px;">RSVP</span>

  <div class="art art-batter" role="img" aria-label="Navy silhouette of a batter swinging"></div>
  <div class="art art-bats" role="img" aria-label="Two crossed wooden baseball bats with a baseball above the crossing"></div>
  <div class="art art-fielder" role="img" aria-label="Navy silhouette of a fielder throwing"></div>
</main>
</body>
</html>
```